Logo and Flyer for Co-Branded Comedy Show

Graphic designer needed to create a promotional flyer for a comedy show. Two different comedy shows, with distinct branding, are joining forces to create a combined show. (co-branded logo to be included is attached.)

The design of the promotional materials should be a modern take on a vintage poster a la Quirkline Jamboree. We'd like it to be a vintage look with a modern twist (I have attached the Quirkline Jamboree Flyer for reference - marked up with info for our show) Filename: HMLVRW Flyer Mark Up

Images of the two hosts are attached: Filenames:

Our show will be in a theater, so if it can play off a playbill that would be great. I have attached examples of the clean look that we like, as well as some vintage theater flyers. We'd like to stay on the lighter side of the color palette (light gray, blues, etc. which is in line with the Hollowmere, Laugh Loud flyer) Filename: HMLV RW Flyer Direction

Current Branding of the individual Shows
I have attached the current promo materials for the individual shows, so you have a sense of the color palette and logo treatment.

The deliverable:
1 flyer vertical, 1 flyer horizontal - same design/concept but in 2 orientation (vertical and horizontal) horizontal will be used for web.
***This flyer will include the co-branded logo seen attached - Hollowmere Laugh Loud Rolls With It (individual logos already created and attached) - Download PSD File here: http://lnkbox.example/HMLVRW

Industry/Entity Type

Graphic Designer

Colors
0493cd
85cae6
ecf7fb
f5f5f5
ffffff
606060
fbfbfb
0255a3
3176b5

Requirements
Must have
• Vintage look with a modern twist
• Vertical and horizontal options

```html
<!DOCTYPE html>
<html lang="en">
<head>
<meta charset="utf-8">
<title>Hollowmere Laugh Loud — Rolls With It Comedy Show</title>
<link rel="stylesheet" href="https://fonts.googleapis.com/css2?family=Archivo+Black&family=Oswald:wght@400;500;600;700&family=Rye&family=Cinzel:wght@700&family=Open+Sans:ital,wght@0,400;0,600;1,400&display=swap">
<style>
  :root {
    --backdrop: #5c6068;
    --paper-edge: #ececec;
    --deep-blue: #1f5189;
    --shadow-blue: #173f6c;
    --mid-blue: #3176b5;
    --ink: #3c3c3c;
    --grey: #606060;
    --white: #ffffff;
  }
  * { box-sizing: border-box; margin: 0; padding: 0; }
  html, body { width: 1200px; height: 1000px; overflow: hidden; background: var(--backdrop); }
  .poster {
    position: absolute; left: 291px; top: 20px; width: 618px; height: 955px;
    background: radial-gradient(ellipse at center, var(--white) 30%, var(--paper-edge) 100%);
    overflow: hidden;
  }
  .abs { position: absolute; }
  .center { left: 0; right: 0; text-align: center; }

  .presenter { top: 28px; display: flex; justify-content: center; align-items: center; gap: 14px; }
  .dots { width: 150px; height: 6px; background-image: radial-gradient(circle, var(--ink) 1.2px, transparent 1.4px); background-size: 6px 6px; }
  .presenter-name { font-family: "Oswald", sans-serif; font-weight: 700; font-size: 22px; line-height: 1; color: #111; text-align: center; letter-spacing: .5px; }
  .presenter-name small { display: block; font-size: 10px; line-height: 1; letter-spacing: 1px; font-weight: 600; }
  .presents { top: 80px; font-family: "Open Sans", sans-serif; font-style: italic; font-size: 15px; line-height: 16px; color: var(--deep-blue); }

  .show-mark { top: 98px; left: 189px; width: 244px; height: 52px; background: var(--deep-blue); border-radius: 26px;
    font-family: "Archivo Black", sans-serif; font-size: 30px; color: var(--white); text-align: center; line-height: 52px; }

  .cloud { left: 0; top: 165px; }
  .tagline { top: 190px; font-family: "Cinzel", serif; font-size: 18px; line-height: 20px; color: var(--white); letter-spacing: 1px; }
  .title { top: 214px; font-family: "Archivo Black", sans-serif; color: var(--white); font-size: 66px; line-height: 70px;
    text-shadow: 3px 3px 0 var(--shadow-blue), 5px 5px 0 var(--shadow-blue); letter-spacing: 1px; }
  .subtitle-band { top: 366px; left: 189px; width: 244px; height: 40px; background: var(--deep-blue); border-radius: 8px;
    font-family: "Cinzel", serif; font-size: 24px; color: var(--white); text-align: center; line-height: 40px; }

  .portrait { border: 3px solid #222; border-radius: 50%; }
  .portrait.side { width: 118px; height: 142px; top: 474px; background: linear-gradient(180deg, #c9cdd3, #7a7f86 70%, #3b3f45); }
  .portrait.side.left { left: 40px; }
  .portrait.side.right { left: 460px; background: linear-gradient(180deg, #d9d6cf, #6a5a4c 60%, #2f6f6f); }
  .portrait.main { left: 166px; top: 432px; width: 286px; height: 170px; background: linear-gradient(180deg, #e4e4e4, #8a7a70 55%, #3a3a3e); }
  .role-tag { font-family: "Oswald", sans-serif; font-size: 13px; line-height: 18px; color: var(--ink); background: var(--white); border: 2px solid #222;
    border-radius: 10px; padding: 0 8px; top: 456px; }
  .role-tag.left { left: 68px; }
  .role-tag.right { left: 488px; }
  .cohost-name { top: 622px; width: 150px; font-family: "Rye", serif; font-size: 15px; line-height: 16px; color: var(--ink); text-align: center; }
  .cohost-name.left { left: 24px; }
  .cohost-name.right { left: 444px; }
  .credit { top: 657px; width: 190px; font-family: "Open Sans", sans-serif; font-size: 9px; line-height: 11px; color: #222; text-align: center; }
  .credit.left { left: 4px; }
  .credit.right { left: 424px; }
  .featuring-label { top: 606px; font-family: "Oswald", sans-serif; font-size: 13px; line-height: 14px; color: #222; }
  .headliner { top: 622px; font-family: "Rye", serif; font-size: 40px; line-height: 46px; color: #222; font-weight: 400; }

  .one-night { top: 690px; display: flex; justify-content: center; align-items: center; gap: 12px;
    font-family: "Oswald", sans-serif; font-weight: 600; font-size: 23px; line-height: 26px; color: var(--ink); }
  .one-night .dots { width: 120px; height: 12px; background-size: 5px 5px; background-image: radial-gradient(circle, #777 1px, transparent 1.3px); }
  .date { top: 720px; font-family: "Oswald", sans-serif; font-weight: 600; font-size: 50px; line-height: 52px; color: var(--ink); letter-spacing: -.5px; }

  .lineup-label { top: 777px; left: 28px; font-family: "Open Sans", sans-serif; font-style: italic; font-size: 17px; line-height: 18px; color: var(--mid-blue); }
  .lineup-rule { top: 784px; left: 96px; right: 0; height: 9px; background: var(--deep-blue); }
  .lineup { top: 801px; left: 24px; right: 24px; display: flex; justify-content: space-between; align-items: center; list-style: none;
    font-family: "Oswald", sans-serif; font-weight: 600; font-size: 18px; line-height: 19px; color: var(--deep-blue); text-align: center; text-transform: uppercase; }
  .venue { top: 847px; left: 0; right: 0; height: 33px; background: var(--deep-blue); border-top: 2px solid var(--mid-blue); border-bottom: 2px solid var(--mid-blue);
    font-family: "Oswald", sans-serif; font-size: 20px; color: var(--white); text-align: center; line-height: 29px; }
  .tickets { top: 898px; font-family: "Open Sans", sans-serif; font-size: 10px; line-height: 12px; color: var(--grey); }
  .website { top: 912px; font-family: "Open Sans", sans-serif; font-size: 18px; line-height: 22px; color: var(--grey); }
</style>
</head>
<body>
<main class="poster">
  <div class="abs center presenter">
    <span class="dots"></span>
    <div class="presenter-name">PALE LANTERN<small>ENTERTAINMENT</small></div>
    <span class="dots"></span>
  </div>
  <p class="abs center presents">presents</p>
  <div class="abs show-mark">Hollowmere</div>

  <svg class="abs cloud" width="618" height="250" viewBox="0 0 618 250" aria-hidden="true">
    <path d="M14 110 C4 60 80 38 160 42 C230 18 270 12 309 14 C350 12 392 18 458 42 C538 38 614 60 604 110 C614 170 560 200 490 206 C430 236 360 244 309 242 C258 244 188 236 128 206 C58 200 4 170 14 110 Z" fill="#1f5189"/>
  </svg>
  <p class="abs center tagline">LAUGH LOUD!!</p>
  <h1 class="abs center title">ROLLS<br>WITH IT</h1>
  <div class="abs subtitle-band">Comedy Show</div>

  <div class="abs portrait side left" role="img" aria-label="Portrait photo of co-host Vexo Rhymes"></div>
  <div class="abs portrait main" role="img" aria-label="Portrait photo of featured comedian Renwick"></div>
  <div class="abs portrait side right" role="img" aria-label="Portrait photo of co-host Delia Marvost"></div>
  <span class="abs role-tag left">CO-HOST</span>
  <span class="abs role-tag right">CO-HOST</span>
  <p class="abs cohost-name left">VEXO<br>RHYMES</p>
  <p class="abs cohost-name right">DELIA<br>MARVOST</p>
  <p class="abs credit left">(Late Lounge, Wave 94)</p>
  <p class="abs credit right">(Laugh Channel, City Comedy Fest)</p>
  <p class="abs center featuring-label">FEATURING</p>
  <h2 class="abs center headliner">RENWICK</h2>

  <div class="abs center one-night"><span class="dots"></span>ONE NIGHT ONLY<span class="dots"></span></div>
  <p class="abs center date">SATURDAY, AUGUST 22, 2015</p>

  <p class="abs lineup-label">featuring</p>
  <div class="abs lineup-rule"></div>
  <ul class="abs lineup">
    <li>Tobin<br>Lasker</li>
    <li>Hollis<br>Greenvale</li>
    <li>Corwin<br>Macalder</li>
    <li>Mina<br>Travko</li>
    <li>Renwick</li>
    <li>Dale<br>Normick</li>
  </ul>
  <p class="abs venue">Carousel Theater | 214 Meridian, Hollowmere, NY 10000</p>
  <p class="abs center tickets">For Tickets and More Information Please Visit</p>
  <p class="abs center website">www.HMLVRW.com</p>
</main>
</body>
</html>
```